ALL TEXT Social Media Graphics

We are looking for a series of social media graphics for Instagram (new size: 4:5 (1080 x 1350 pixels) ratio that are ALL TEXT. We want the following quotes below on each graphic; one quote per graphic. AND, In very small letters at the bottom of each graphic, add @PaulaWrenLive
The look and feel of these graphics should be complimentary to the color palette attached below; but keep them simple. But the design is up to you; at the end of this document, I provided various samples of all text graphics that I like as examples.
The Quotes are in the attached WORD document
women trying to lose weight

```html
<!DOCTYPE html>
<html lang="en">
<head>
<meta charset="utf-8">
<title>All Text Social Graphics</title>
<link rel="stylesheet" href="https://fonts.googleapis.com/css2?family=Bebas+Neue&family=Noto+Sans:wght@400;600;700&family=Playfair+Display:ital@1&display=swap">
<style>
  :root {
    --wine: #b0124f;
    --rose: #e4457f;
    --ink: #111111;
    --frame: #fbc6e3;
    --blush-top: #ffffff;
    --blush-bottom: #fcc3e3;
    --page: #ffffff;
  }
  * { box-sizing: border-box; margin: 0; padding: 0; }
  html, body {
    width: 1200px; height: 933px; overflow: hidden;
    background: var(--page);
  }
  .sheet { position: relative; width: 1200px; height: 933px; }
  .post {
    position: absolute; width: 288px; height: 360px; overflow: hidden;
    border: 2px solid var(--frame); border-bottom: none;
    background: linear-gradient(180deg, var(--blush-top) 6%, #fde6f1 40%, var(--blush-bottom) 100%);
    font-family: "Noto Sans", sans-serif; color: var(--ink);
    --pad: 16px;
  }
  .post > * { position: absolute; left: var(--pad); white-space: nowrap; }
  .post--1 { left: 99px; top: 74px; --pad: 15px; }
  .post--2 { left: 456px; top: 74px; --pad: 11px; }
  .post--3 { left: 813px; top: 74px; --pad: 13px; }
  .post--4 { left: 99px; top: 500px; --pad: 12px; }
  .post--5 { left: 456px; top: 500px; --pad: 10px; }

  .headline {
    font-family: "Bebas Neue", sans-serif; color: var(--wine);
    font-weight: 400; letter-spacing: 0.3px;
  }
  .headline .accent { color: var(--rose); }
  .subhead {
    font-family: "Bebas Neue", sans-serif; color: var(--rose);
    font-size: 32px; line-height: 32px;
  }
  .body { font-size: 15px; line-height: 20px; }
  .body--bold { font-weight: 700; letter-spacing: 0.4px; }
  .body--semi { font-weight: 600; font-size: 14.5px; line-height: 22.5px; }
  .body--airy { letter-spacing: 0.6px; line-height: 23.6px; }
  .body--large { font-size: 20px; line-height: 25.2px; }
  .cta { font-size: 21px; font-weight: 700; letter-spacing: 0.6px; line-height: 30px; }
  .cta--light { font-weight: 400; font-size: 25px; letter-spacing: 0; }
  .cta .keyword {
    font-family: "Bebas Neue", sans-serif; color: var(--wine);
    font-weight: 400; font-size: 32px; line-height: 1; letter-spacing: 0.5px;
  }
  .tagline {
    font-family: "Playfair Display", serif; font-style: italic;
    color: var(--rose); font-size: 18px; line-height: 27px;
  }
  .tagline--large { font-size: 25px; line-height: 33px; }
  .link { color: var(--rose); font-weight: 700; font-size: 21px; line-height: 26px; display: flex; align-items: center; gap: 6px; }
  .handle { font-size: 12px; line-height: 16px; letter-spacing: 0.3px; }
  .handle--lg { font-size: 13px; }
</style>
</head>
<body>
<main class="sheet">

  <section class="post post--1">
    <h2 class="headline" style="top:29px;font-size:55px;line-height:44px">This summer<br>ain’t over—</h2>
    <p class="body body--bold" style="top:128px">and neither are your body<br>goals. Drop 30 pounds<br>with the Summer Glow<br>Reset.</p>
    <p class="cta" style="top:219px">Comment <span class="keyword">“Hot Girl”</span></p>
    <p class="tagline" style="top:250px">to get the plan</p>
    <p class="handle" style="top:292px">@PaulaWrenLive</p>
  </section>

  <section class="post post--2">
    <h2 class="headline" style="top:9px;font-size:51px;line-height:45.6px">If your<br>goal is a</h2>
    <p class="subhead" style="top:105px">Tiny waist,<br>flat belly, and<br>30 pounds down—</p>
    <p class="body body--airy" style="top:211px">this is the plan.</p>
    <p class="cta" style="top:239px">Comment <span class="keyword">“Summer”</span></p>
    <p class="tagline" style="top:269px">to join the Summer<br>Glow Reset!</p>
    <p class="handle" style="top:331px">@PaulaWrenLive</p>
  </section>

  <section class="post post--3">
    <h2 class="headline" style="top:39px;font-size:53px;line-height:48px">There’s still<br>time to drop</h2>
    <p class="body body--airy" style="top:145px">the 30 pounds and<br>slay this summer.<br>The Summer Glow Reset<br>has the blueprint.</p>
    <p class="cta" style="top:253px">Comment <span class="keyword">“Hot Girl”!</span></p>
    <p class="handle" style="top:299px">@PaulaWrenLive</p>
  </section>

  <section class="post post--4">
    <h2 class="headline" style="top:21px;font-size:48px;line-height:50px;letter-spacing:0">You don’t need<br>another diet—</h2>
    <p class="body body--semi" style="top:127px">you need a system that works.<br>Drop 30 pounds with the Summer<br>Glow Reset.</p>
    <p class="cta cta--light" style="top:205px">Comment <span class="keyword" style="font-size:28px">“Summer”</span> to</p>
    <p class="link" style="top:248px">start now
      <svg width="14" height="14" viewBox="0 0 14 14" aria-hidden="true"><path d="M2 2l5 5-5 5M7 2l5 5-5 5" fill="none" stroke="currentColor" stroke-width="1.8"/></svg>
    </p>
    <p class="handle handle--lg" style="top:293px">@PaulaWrenLive</p>
  </section>

  <section class="post post--5">
    <h2 class="headline" style="top:22px;font-size:33px;line-height:33.5px;letter-spacing:0">You can absolutely<br>be down <span class="accent">20–30 pounds</span></h2>
    <p class="body body--large" style="top:96px">by end of summer.<br>All it takes is the<br>right plan—and<br>you’ve found it.</p>
    <p class="cta cta--light" style="top:203px">Comment <span class="keyword" style="font-size:31px">“Hot Girl”</span></p>
    <p class="tagline tagline--large" style="top:236px">for the Summer<br>Glow Reset!</p>
    <p class="handle handle--lg" style="top:320px">@PaulaWrenLive</p>
  </section>

</main>
</body>
</html>
```